Quillbase Design Project - App Review

Take a look at this website, gridvault.example. We are creating something very similar to this, four pages are required. The name of our website is BrightPickDigest.example
1) The home page which highlights, app of the day, a carousel which highlights featured apps, and top apps in different categories
2) Single App Page - This page will details the app that is selected, app icon, app description, app ratings, and other information you can find on an app page in the lumora market
3) A page that list all the apps in a category, for example if the user select, "100 top apps" the page that will display the list of 100 apps, 10 per page, summary of description, a small icon, screenshot etc for each app
4) Review Page - where we review an app of the day, including screenshots, videos, text reviews etc
I do not have any logo at the moment, use these as nav links; home, my apps, reviews, blog and contact. Thank you.
I will like to see a nice creativity. I am open to a very beautiful color combinations. Thank you
Target Market(s)
App shoppers, people that are looking for new apps, discounted apps etc
Industry/Entity Type
Store
Look and feel

```html
<!DOCTYPE html>
<html lang="en">
<head>
<meta charset="utf-8">
<title>App Review</title>
<link href="https://fonts.googleapis.com/css2?family=Oswald:wght@400;500&family=Source+Sans+3:wght@400;600&display=swap" rel="stylesheet">
<style>
:root{
  --blue:#1ea3e3;
  --blue-dark:#0f78b5;
  --btn-top:#3cb6ee;
  --btn-bottom:#137cbb;
  --ink:#555;
  --ink-soft:#6a6a6a;
  --page:#f7f7f7;
  --band:#e4e4e4;
  --footer:#363636;
  --footer-deep:#222;
  --field:#151515;
  --white:#fff;
}
*{box-sizing:border-box;margin:0;padding:0}
html,body{width:967px;height:1200px;overflow:hidden}
body{position:relative;background:var(--page);font-family:"Source Sans 3",sans-serif;color:var(--ink)}
.abs{position:absolute}
.top-band{left:0;top:0;width:967px;height:360px;background:linear-gradient(#f8f8f8,var(--band))}
.brand{left:97px;top:32px;display:flex;align-items:center;gap:12px}
.brand-mark{width:55px;height:55px;border-radius:50%;background:#5c6670}
.brand-name{font-family:"Oswald",sans-serif;font-weight:400;font-size:36px;color:var(--blue)}
.search{left:668px;top:42px;width:213px;height:29px;display:flex}
.search-field{flex:1;background:#efefef;border:1px solid #e2e2e2;font-size:11px;color:#666;padding:7px 9px}
.search-btn{width:29px;height:29px;background:linear-gradient(#4a4a4a,#1c1c1c)}
.nav{left:90px;top:124px;display:flex;align-items:center;font-size:15px;color:#555}
.nav a{text-decoration:none;color:inherit;margin-right:38px}
.nav .current{background:linear-gradient(var(--btn-top),var(--btn-bottom));color:var(--white);padding:7px 13px;border-radius:2px;margin-right:28px}
.talk{right:84px;top:100px;text-align:right;font-family:"Oswald",sans-serif}
.talk-label{font-size:24px;color:#777;line-height:1.2}
.talk-phone{font-size:23px;color:var(--blue);font-weight:500;line-height:1.2}
.slider{left:71px;top:166px;width:825px;height:303px;background:#e6e6e6;border-radius:3px}
.slide{left:78px;top:174px;width:809px;height:289px;border-radius:4px;background:radial-gradient(circle at 30% 50%,#8ed4ef,#2b95d1 55%,#1170b6)}
.slide-art{left:150px;top:188px;width:285px;height:268px;border-radius:8px;background:linear-gradient(135deg,#d9dde0,#4b5258 60%,#7fbf3c)}
.slide-title{left:444px;top:226px;font-family:"Oswald",sans-serif;font-size:36px;color:var(--white);font-weight:400}
.slide-text{left:447px;top:281px;width:322px;font-size:10.6px;line-height:17px;color:var(--white)}
.slide-btn{left:446px;top:352px;width:121px;height:30px;border-radius:3px;background:linear-gradient(var(--btn-top),var(--btn-bottom));color:var(--white);font-family:"Oswald",sans-serif;font-size:19px;text-align:center;line-height:30px}
.arrow{width:29px;height:29px;border-radius:50%;background:#2f3c47;border:1px solid #6d7c87}
.feature{width:232px}
.feature-title{font-family:"Oswald",sans-serif;font-size:22px;color:var(--blue);font-weight:400;letter-spacing:.2px;white-space:nowrap}
.feature-icon{width:42px;height:42px;border-radius:50%;background:var(--blue)}
.feature-text{font-size:10.9px;line-height:20px;color:var(--ink-soft);font-weight:400;margin-top:10px;width:232px}
.btn{display:block;width:80px;height:29px;border-radius:4px;background:linear-gradient(var(--btn-top),var(--btn-bottom));color:var(--white);font-family:"Oswald",sans-serif;font-size:14px;text-align:center;line-height:29px;box-shadow:0 3px 4px rgba(0,0,0,.18)}
.divider{width:1px;height:170px;background:linear-gradient(transparent,#ddd,transparent)}
.section-title{left:0;width:967px;top:642px;text-align:center;font-family:"Oswald",sans-serif;font-size:19px;font-weight:400;color:var(--blue)}
.mini-arrow{width:17px;height:17px;border-radius:50%;background:#3a3a3a}
.card{width:194px}
.card-frame{height:134px;background:var(--white);border:1px solid #ddd;padding:8px;box-shadow:0 3px 5px rgba(0,0,0,.08)}
.card-img{width:100%;height:100%}
.card-title{font-size:15px;font-weight:400;color:var(--blue);margin:16px 0 3px 9px}
.card-text{font-size:9.6px;font-weight:400;line-height:15px;color:#444;margin-left:9px;width:180px}
.footer{left:0;top:1007px;width:967px;height:153px;background:var(--footer)}
.footer-bottom{left:0;top:1160px;width:967px;height:40px;background:var(--footer-deep)}
.up{left:469px;top:990px;width:30px;height:30px;border-radius:50%;background:var(--footer)}
.foot-title{font-family:"Oswald",sans-serif;font-size:19px;color:#ddd;font-weight:400}
.quick-links{list-style:none;font-size:13px;line-height:18.5px;color:#eee;margin-top:10px;margin-left:3px}
.social{display:flex;align-items:center;gap:12px}
.social-dot{width:36px;height:36px;border-radius:50%}
.social-main{font-family:"Oswald",sans-serif;font-size:15px;color:#eee}
.social-sub{font-family:"Oswald",sans-serif;font-size:12px;color:#ddd}
.field{background:var(--field);border-radius:5px;font-size:9px;color:#aaa;padding:9px 11px;font-family:"Oswald",sans-serif}
.submit{border-radius:5px;background:linear-gradient(var(--btn-top),var(--btn-bottom));color:var(--white);font-family:"Oswald",sans-serif;font-size:14px;text-align:center;line-height:28px}
.copyright{left:580px;top:1174px;font-size:10px;color:#ccc}
</style>
</head>
<body>
<div class="abs top-band"></div>

<header>
  <div class="abs brand"><span class="brand-mark"></span><span class="brand-name">App Review</span></div>
  <div class="abs search"><div class="search-field">Search</div>
    <div class="search-btn"><svg width="29" height="29" viewBox="0 0 29 29"><circle cx="12" cy="12" r="4.5" fill="none" stroke="#fff" stroke-width="2"/><line x1="15.5" y1="15.5" x2="21" y2="20" stroke="#fff" stroke-width="2.5"/></svg></div>
  </div>
  <nav class="abs nav"><a class="current">Home</a><a>My apps</a><a>Reviews</a><a>Blog</a><a>Contact</a></nav>
  <div class="abs talk"><div class="talk-label">Want to Talk?</div><div class="talk-phone">1800-555-0199</div></div>
</header>

<section>
  <div class="abs slider"></div>
  <div class="abs slide"></div>
  <div class="abs slide-art" role="img" aria-label="Smartphones with app icons, speaker, film reel, game controller and a green app badge"></div>
  <h1 class="abs slide-title">Pocket Apps.</h1>
  <p class="abs slide-text">Praesent pellentesque ullamcorper nulla, et molestie justo dapibus non. Phasellus tempor dapibus varius. Nulla facilisi. Vivamus pulvinar dapibus laoreet.</p>
  <div class="abs slide-btn">Get it Now</div>
  <div class="abs arrow" style="left:99px;top:304px"><svg width="27" height="27" viewBox="0 0 27 27"><polyline points="15,8 10,13.5 15,19" fill="none" stroke="#fff" stroke-width="1.5"/></svg></div>
  <div class="abs arrow" style="left:836px;top:304px"><svg width="27" height="27" viewBox="0 0 27 27"><polyline points="12,8 17,13.5 12,19" fill="none" stroke="#fff" stroke-width="1.5"/></svg></div>
</section>

<section>
  <div class="abs divider" style="left:341px;top:470px"></div>
  <div class="abs divider" style="left:624px;top:470px"></div>

  <div class="abs feature" style="left:91px;top:480px">
    <h2 class="feature-title">APP OF THE DAY</h2>
    <p class="feature-text">Sed ut perspiciatis unde omnis iste natus error sit voluptatem accusantium doloremque lau-dantium, totam rem aperiam,</p>
  </div>
  <div class="abs feature-icon" style="left:283px;top:479px"><svg width="42" height="42" viewBox="0 0 42 42"><path d="M19 27v-11a2 2 0 0 1 4 0v6l5 1v6l-3 3h-5z" fill="none" stroke="#fff" stroke-width="1.5"/></svg></div>
  <span class="abs btn" style="left:88px;top:588px">READ MORE</span>

  <div class="abs feature" style="left:369px;top:480px">
    <h2 class="feature-title">FEATURED APPS</h2>
    <p class="feature-text">Sed ut perspiciatis unde omnis iste natus error sit voluptatem accusantium doloremque lau-dantium, totam rem aperiam,</p>
  </div>
  <div class="abs feature-icon" style="left:561px;top:479px"><svg width="42" height="42" viewBox="0 0 42 42"><rect x="16" y="14" width="10" height="13" fill="none" stroke="#fff" stroke-width="1.5"/><rect x="19" y="17" width="8" height="11" fill="#fff"/></svg></div>
  <span class="abs btn" style="left:367px;top:588px">READ MORE</span>

  <div class="abs feature" style="left:652px;top:480px">
    <h2 class="feature-title">MOST RECENT NEWS</h2>
    <p class="feature-text">Sed ut perspiciatis unde omnis iste natus error sit voluptatem accusantium doloremque lau-dantium, totam rem aperiam,</p>
  </div>
  <div class="abs feature-icon" style="left:843px;top:479px"><svg width="42" height="42" viewBox="0 0 42 42"><rect x="15" y="15" width="12" height="8" fill="#fff"/><line x1="21" y1="23" x2="21" y2="28" stroke="#fff" stroke-width="1.5"/></svg></div>
  <span class="abs btn" style="left:654px;top:588px">READ MORE</span>
</section>

<section>
  <h2 class="abs section-title">TOP APPS IN DIFFERENT CATEGORIES</h2>
  <div class="abs mini-arrow" style="left:850px;top:642px"><svg width="17" height="17" viewBox="0 0 17 17"><polyline points="10,5 7,8.5 10,12" fill="none" stroke="#fff" stroke-width="1.2"/></svg></div>
  <div class="abs mini-arrow" style="left:871px;top:642px"><svg width="17" height="17" viewBox="0 0 17 17"><polyline points="7,5 10,8.5 7,12" fill="none" stroke="#fff" stroke-width="1.2"/></svg></div>

  <article class="abs card" style="left:81px;top:682px">
    <div class="card-frame"><div class="card-img" role="img" aria-label="Dark photo of colored pencil strokes with a plus button" style="background:linear-gradient(135deg,#2a2a2a,#3d3d3d)"></div></div>
    <h3 class="card-title">Web Design</h3>
    <p class="card-text">Lorem ipsum dolor sit amet, consectetu adipiscing elit, sed diam nonummy nibh euismod tincidunt ut laoreet iam.</p>
  </article>
  <article class="abs card" style="left:285px;top:682px">
    <div class="card-frame"><div class="card-img" role="img" aria-label="Tablet and phone showing a travel photo gallery" style="background:linear-gradient(135deg,#f3f3f3,#c9c9c9)"></div></div>
    <h3 class="card-title">Pocket Apps</h3>
    <p class="card-text">Lorem ipsum dolor sit amet, consectetu adipiscing elit, sed diam nonummy nibh euismod tincidunt ut laoreet iam.</p>
  </article>
  <article class="abs card" style="left:489px;top:682px">
    <div class="card-frame"><div class="card-img" role="img" aria-label="Tree illustration with colorful app symbols as leaves" style="background:radial-gradient(circle,#e9cfd6,#fdfdfd 70%)"></div></div>
    <h3 class="card-title">Mobile Apps</h3>
    <p class="card-text">Lorem ipsum dolor sit amet, consectetu adipiscing elit, sed diam nonummy nibh euismod tincidunt ut laoreet iam.</p>
  </article>
  <article class="abs card" style="left:694px;top:682px">
    <div class="card-frame"><div class="card-img" role="img" aria-label="Phone with red envelope and flying letters" style="background:linear-gradient(#cfcfcf,#e8e8e8)"></div></div>
    <h3 class="card-title">Email</h3>
    <p class="card-text">Lorem ipsum dolor sit amet, consectetu adipiscing elit, sed diam nonummy nibh euismod tincidunt ut laoreet iam.</p>
  </article>

  <span class="abs btn" style="left:84px;top:940px">READ MORE</span>
  <span class="abs btn" style="left:289px;top:940px">READ MORE</span>
  <span class="abs btn" style="left:493px;top:940px">READ MORE</span>
  <span class="abs btn" style="left:697px;top:940px">READ MORE</span>
</section>

<footer>
  <div class="abs footer"></div>
  <div class="abs up"><svg width="30" height="30" viewBox="0 0 30 30"><polyline points="10,17 15,12 20,17" fill="none" stroke="#ddd" stroke-width="1.5"/></svg></div>

  <div class="abs" style="left:87px;top:1012px">
    <h3 class="foot-title">Quick Links</h3>
    <ul class="quick-links"><li>Home</li><li>My Apps</li><li>Reviews</li><li>Blog</li><li>Contact</li></ul>
  </div>

  <div class="abs" style="left:306px;top:1014px">
    <h3 class="foot-title">Follow Us</h3>
    <div class="social" style="margin-top:14px;margin-left:-6px"><span class="social-dot" style="background:#e0352b"></span><div><div class="social-main">We are on Circlenet</div><div class="social-sub">Add to your circle</div></div></div>
    <div class="social" style="margin-top:14px;margin-left:-6px"><span class="social-dot" style="background:#2aa6e3"></span><div><div class="social-main">We are on Chirpline</div><div class="social-sub">Follow me</div></div></div>
  </div>

  <h3 class="abs foot-title" style="left:555px;top:1017px">Contact Us</h3>
  <div class="abs field" style="left:549px;top:1051px;width:103px;height:26px">NAME</div>
  <div class="abs field" style="left:658px;top:1051px;width:103px;height:26px">EMAIL</div>
  <div class="abs field" style="left:549px;top:1083px;width:212px;height:32px">MESSAGE</div>
  <div class="abs submit" style="left:768px;top:1084px;width:79px;height:28px">SUBMIT</div>

  <div class="abs footer-bottom"></div>
  <p class="abs copyright">Copyright © 2103 &nbsp;www.appreview.example &nbsp;&nbsp;All rights reserved.</p>
</footer>
</body>
</html>
```